Willowmere Pet Farewells - business cards & brand stationary

We already have a logo and the colors and a website. Need a business card designed that will be able to customized to multiple veterinarians who will be partnering with us. The feel needs to be compassionate, comforting with our tagline 'A Gift of Love at Home'. It will be 2 sides.
On the back our platform/partner vets will be customizing each business card with their own service areas, phone numbers, name and title. On the front, i would like to see experimentation with use of our photos, the logo, tagline and a description 'Peaceful and Compassionate At-Home Pet Euthanasia'

```html
<!DOCTYPE html>
<html lang="en">
<head>
<meta charset="utf-8">
<title>Willowmere Pet Farewells – Business Card</title>
<link rel="stylesheet" href="https://fonts.googleapis.com/css2?family=Poppins:ital,wght@0,400;0,600;1,500;1,600&family=Raleway:ital,wght@1,300&display=swap">
<style>
  :root {
    --page-bg: #e3e6ec;
    --card-bg: #f8f9fc;
    --brand-blue: #7496c0;
    --soft-blue: #c9d4e4;
    --mist-blue: #dbe3ee;
    --ink: #2f3b50;
    --ink-soft: #3d4658;
    --white: #ffffff;
  }
  * { box-sizing: border-box; margin: 0; padding: 0; }
  html, body { width: 777px; height: 1200px; overflow: hidden; }
  body {
    background: var(--page-bg);
    font-family: "Poppins", Arial, sans-serif;
    position: relative;
  }
  .card {
    position: absolute;
    top: 312px;
    width: 330px;
    height: 577px;
    background: var(--card-bg);
    overflow: hidden;
    box-shadow: 0 2px 6px rgba(40, 50, 70, 0.18);
  }
  .card--front { left: 40px; }
  .card--back { left: 407px; }

  .brand {
    position: absolute;
    left: 0; right: 0;
    display: flex;
    flex-direction: column;
    align-items: center;
  }
  .card--front .brand { top: 100px; }
  .card--back .brand { top: 70px; }
  .brand__lockup {
    display: flex;
    align-items: center;
    gap: 8px;
  }
  .brand__mark {
    width: 26px; height: 26px;
    background: var(--brand-blue);
    border-radius: 4px;
  }
  .brand__name {
    font-family: "Poppins", Arial, sans-serif;
    font-weight: 600;
    font-size: 18px;
    color: var(--brand-blue);
    letter-spacing: -0.2px;
  }
  .brand__tagline {
    margin-top: 10px;
    font-family: "Raleway", Arial, sans-serif;
    font-style: italic;
    font-weight: 300;
    font-size: 23px;
    color: var(--brand-blue);
  }

  .band {
    position: absolute;
    left: 0; right: 0;
    height: 56px;
    background: var(--brand-blue);
    color: var(--white);
    font-style: italic;
    font-weight: 600;
    font-size: 14.5px;
    line-height: 19px;
    text-align: center;
    display: flex;
    flex-direction: column;
    justify-content: center;
  }
  .card--front .band { top: 206px; }
  .card--back .band { top: 200px; }

  .hero-circle {
    position: absolute;
    left: 68px; top: 400px;
    width: 300px; height: 300px;
    border-radius: 50%;
    background: var(--soft-blue);
  }
  .hero-photo {
    position: absolute;
    left: 74px; top: 286px;
    width: 256px; height: 291px;
    border-radius: 110px 90px 0 0;
    background: linear-gradient(160deg, #2b3348 0%, #1c2233 55%, #3a4257 100%);
  }

  .back-photo {
    position: absolute;
    left: 0; top: 256px;
    width: 330px; height: 321px;
    background: linear-gradient(150deg, var(--mist-blue) 0%, #cfd9e7 50%, #e4eaf2 100%);
  }
  .vet {
    position: absolute;
    left: 41px; top: 318px;
  }
  .vet__name {
    font-weight: 600;
    font-size: 20px;
    line-height: 24px;
    color: var(--ink);
  }
  .vet__area {
    font-style: italic;
    font-weight: 500;
    font-size: 11.6px;
    color: var(--ink-soft);
    letter-spacing: 0.2px;
  }
  .contact {
    position: absolute;
    left: 41px; top: 387px;
    list-style: none;
  }
  .contact__item {
    display: flex;
    align-items: center;
    gap: 10px;
    height: 23.5px;
    font-size: 14px;
    color: var(--ink-soft);
  }
  .contact__icon { width: 16px; height: 16px; flex: none; }

  .social {
    position: absolute;
    right: -40px; bottom: -60px;
    width: 160px; height: 160px;
    border-radius: 50%;
    background: var(--white);
  }
  .social__links {
    position: absolute;
    right: 24px; bottom: 24px;
    display: flex;
    gap: 6px;
  }
  .social__dot {
    width: 24px; height: 24px;
    border-radius: 50%;
    background: var(--brand-blue);
  }
</style>
</head>
<body>

<section class="card card--front" aria-label="Business card front">
  <div class="brand">
    <div class="brand__lockup">
      <span class="brand__mark"></span>
      <span class="brand__name">Willowmere Pet Farewells</span>
    </div>
    <p class="brand__tagline">A gift of love at home.</p>
  </div>
  <div class="band">
    <span>Peaceful and Compassionate</span>
    <span>At-Home Pet Euthanasia</span>
  </div>
  <div class="hero-circle"></div>
  <div class="hero-photo" role="img" aria-label="Photo of a senior black dog with a grey muzzle and a white collar, looking upward"></div>
</section>

<section class="card card--back" aria-label="Business card back">
  <div class="brand">
    <div class="brand__lockup">
      <span class="brand__mark"></span>
      <span class="brand__name">Willowmere Pet Farewells</span>
    </div>
    <p class="brand__tagline">A gift of love at home.</p>
  </div>
  <div class="band">
    <span>Peaceful and Compassionate</span>
    <span>At-Home Pet Euthanasia</span>
  </div>
  <div class="back-photo" role="img" aria-label="Soft, pale blue-tinted photo of a tabby cat resting in a person's arms"></div>

  <div class="vet">
    <p class="vet__name">Dr. Elena Marsh</p>
    <p class="vet__area">LARKFIELD, CA &amp; SURROUNDING CITIES</p>
  </div>

  <ul class="contact">
    <li class="contact__item">
      <svg class="contact__icon" viewBox="0 0 16 16"><circle cx="8" cy="8" r="8" fill="#7496c0"/><path d="M5.3 4.2l1.3-.3.8 2-.9.7c.4.9 1.1 1.6 2 2l.7-.9 2 .8-.3 1.3c-.1.4-.5.6-.9.6C7.3 10.2 5.8 8.7 4.6 5c0-.4.3-.7.7-.8z" fill="#fff"/></svg>
      (555) 014 - 2287
    </li>
    <li class="contact__item">
      <svg class="contact__icon" viewBox="0 0 16 16"><circle cx="8" cy="8" r="8" fill="#7496c0"/><path d="M8 3.5a3 3 0 0 0-3 3c0 2.2 3 5.8 3 5.8s3-3.6 3-5.8a3 3 0 0 0-3-3zm0 4.2a1.2 1.2 0 1 1 0-2.4 1.2 1.2 0 0 1 0 2.4z" fill="#fff"/></svg>
      Larkfield, CA
    </li>
    <li class="contact__item">
      <svg class="contact__icon" viewBox="0 0 16 16"><circle cx="8" cy="8" r="8" fill="#7496c0"/><rect x="4" y="5.3" width="8" height="5.6" rx=".6" fill="#fff"/><path d="M4.3 5.6L8 8.5l3.7-2.9" fill="none" stroke="#7496c0" stroke-width=".9"/></svg>
      hello@willowmerepets.com
    </li>
    <li class="contact__item">
      <svg class="contact__icon" viewBox="0 0 16 16"><circle cx="8" cy="8" r="8" fill="#7496c0"/><g fill="none" stroke="#fff" stroke-width=".9"><circle cx="8" cy="8" r="4"/><ellipse cx="8" cy="8" rx="1.7" ry="4"/><path d="M4 8h8"/></g></svg>
      www.willowmerepets.com
    </li>
  </ul>

  <div class="social"></div>
  <div class="social__links" aria-label="Social media links">
    <span class="social__dot"></span>
    <span class="social__dot"></span>
  </div>
</section>

</body>
</html>
```